Invitation Card for Wedding

An invitation card for a wedding is needed.

This competition is to decide the designer who is going to do the real card design. Project budget is in between 30-50 euro. Project time is 1 week after the end of the competition.

You can submit your best available designs for invitation cards. Or desing a card for the weeding of "Selin" and "Burak" with imaginary informations such as place / date / time.

Edit: please check if you can use the figures at the attached images. No need to do a final design for the moment, but I would like to see that you are capable of using and creating nice cards with them.

The competition prize will be distributed fairly.
Good luck

```html
<!DOCTYPE html>
<html lang="en">
<head>
<meta charset="utf-8">
<title>Wedding Invitation</title>
<link rel="stylesheet" href="https://fonts.googleapis.com/css2?family=Roboto+Slab:wght@400&display=swap">
<style>
  :root {
    --backdrop-brown: #5a3a22;
    --stripe-black: #0a0a0a;
    --stripe-white: #ffffff;
    --panel-black: #141414;
    --panel-stripe: rgba(255, 255, 255, 0.06);
    --frame-bronze: #9a7a55;
    --text-white: #ffffff;
    --bloom-magenta: #c8367a;
    --bloom-violet: #8c3fa6;
    --bloom-coral: #ee9c8e;
    --bloom-plum: #a5508c;
  }
  html, body {
    margin: 0;
    padding: 0;
    width: 1200px;
    height: 1200px;
    overflow: hidden;
    background: var(--backdrop-brown);
  }
  .stage {
    position: relative;
    width: 1200px;
    height: 1200px;
    overflow: hidden;
    background: var(--backdrop-brown);
  }
  .invitation-card {
    position: absolute;
    left: 147px;
    top: 137px;
    width: 904px;
    height: 932px;
    overflow: hidden;
    background: repeating-linear-gradient(
      45deg,
      var(--stripe-black) 0 34px,
      var(--stripe-white) 34px 110px
    );
    box-shadow: 0 6px 16px rgba(0, 0, 0, 0.35);
  }
  .message-panel {
    position: absolute;
    left: 146px;
    top: 156px;
    width: 611px;
    height: 619px;
    box-sizing: border-box;
    border: 3px solid var(--frame-bronze);
    background:
      repeating-linear-gradient(45deg, var(--panel-stripe) 0 34px, transparent 34px 110px),
      var(--panel-black);
    box-shadow: 0 4px 14px rgba(0, 0, 0, 0.4);
  }
  .invitation-line {
    position: absolute;
    left: 146px;
    top: 303px;
    width: 611px;
    margin: 0;
    text-align: center;
    color: var(--text-white);
    font-family: "Roboto Slab", Georgia, serif;
    font-weight: 400;
    font-size: 55px;
    line-height: 79px;
  }
  .floral-layer {
    position: absolute;
    left: 0;
    top: 0;
    width: 904px;
    height: 932px;
  }
</style>
</head>
<body>
  <div class="stage">
    <main class="invitation-card">
      <div class="message-panel"></div>
      <p class="invitation-line">You are invited<br>on our Wedding<br>ceremony</p>
      <svg class="floral-layer" viewBox="0 0 904 932" width="904" height="932">
        <defs>
          <linearGradient id="bloom-berry" x1="0" y1="0" x2="1" y2="1">
            <stop offset="0" stop-color="var(--bloom-violet)"/>
            <stop offset="1" stop-color="var(--bloom-magenta)"/>
          </linearGradient>
          <linearGradient id="bloom-bouquet" x1="0" y1="0" x2="1" y2="1">
            <stop offset="0" stop-color="var(--bloom-plum)"/>
            <stop offset="1" stop-color="var(--bloom-coral)"/>
          </linearGradient>
        </defs>
        <g role="img" aria-label="Watercolour spray of magenta flowers and violet leaves">
          <ellipse cx="230" cy="200" rx="170" ry="60" transform="rotate(-22 230 200)" fill="url(#bloom-berry)"/>
        </g>
        <g role="img" aria-label="Small watercolour sprig of magenta flowers and violet leaves">
          <ellipse cx="750" cy="435" rx="52" ry="88" transform="rotate(-15 750 435)" fill="url(#bloom-berry)"/>
        </g>
        <g role="img" aria-label="Watercolour sprig of magenta flowers and violet leaves">
          <ellipse cx="495" cy="790" rx="130" ry="58" transform="rotate(25 495 790)" fill="url(#bloom-berry)"/>
        </g>
        <g role="img" aria-label="Watercolour bouquet of coral blossoms, plum leaves and blue berries">
          <ellipse cx="700" cy="710" rx="165" ry="160" fill="url(#bloom-bouquet)"/>
        </g>
      </svg>
    </main>
  </div>
</body>
</html>
```